Ancient Art and Artifact information website

Hello Designers,
We are starting up a new website who talk abut and discusses an ancient arts artifacts. We would covering a wide range of countries ranging from Egypt, Greece, India, Syria, Rome, etc. My website name Tarn Wisp
Designs that fits with ancient theme and some kind of uniqueness would be accepted.
Requirements:
1) A home page design
2) Sub page design
3) A suitable logo
Sections can be added are featured ancient arts/places with short description followed by a more button, latest news, and comment section.
Add contents if you found relevant for this category of website. Ability to share the information through social media is desired.
Must be a responsive design. I look forward to designs which are mind blowing.
Number of Pages Required
2 page

```html
<!DOCTYPE html>
<html lang="en">
<head>
<meta charset="utf-8">
<title>Tarn Wisp</title>
<link href="https://fonts.googleapis.com/css2?family=Lato:wght@400;700&family=Oswald:wght@300&family=Archivo+Narrow&display=swap" rel="stylesheet">
<style>
:root{
  --orange:#f08a12;
  --sand:#d9b27a;
  --sand-deep:#c99a5c;
  --brown:#8a6438;
  --card:#ececec;
  --text:#333;
  --white:#fff;
}
*{box-sizing:border-box;margin:0;padding:0}
html,body{width:816px;height:1200px;overflow:hidden;background:var(--white)}
body{position:relative;font-family:"Lato",sans-serif;color:var(--text)}
.abs{position:absolute}
.bands{position:absolute;left:0;top:0}
.brand{left:24px;top:78px;width:106px;text-align:center;color:var(--white);font-size:22px;display:flex;align-items:center;justify-content:center;gap:6px}
.brand-mark{width:10px;height:10px;border-radius:50%;background:var(--white)}
.main-nav{left:267px;top:45px;display:flex;gap:25px;font-size:13px}
.main-nav a,.account a{color:var(--white);text-decoration:none}
.main-nav a.current{color:var(--orange)}
.account{left:667px;top:45px;display:flex;gap:12px;font-size:13px;color:var(--orange)}
.section-title{color:var(--orange);font-weight:700;font-size:21px;text-align:center}
.ancient-title{left:560px;top:149px;width:172px}
.card{top:206px;width:185px;height:288px;background:var(--card);box-shadow:0 2px 2px rgba(0,0,0,.25);border-radius:0 0 3px 3px;text-align:center;font-size:11px;line-height:13.5px;color:#444}
.card-img{height:194px;margin-bottom:14px}
.card a{color:var(--orange);text-decoration:none;display:block}
.news-title{left:40px;top:519px;width:212px}
.news-item{left:24px;width:250px}
.news-date{position:absolute;left:0;top:0;width:18px;text-align:center;color:var(--orange);font-family:"Oswald",sans-serif;font-size:17px;line-height:18px}
.news-date span{display:block;font-size:9px;color:#333;line-height:10px}
.news-date::after{content:"";display:block;width:17px;height:2px;background:var(--orange);margin-top:4px}
.news-head{position:absolute;left:46px;top:0;font-family:"Oswald",sans-serif;font-weight:300;font-size:14px;letter-spacing:-.3px;color:#222;white-space:nowrap}
.news-body{position:absolute;left:36px;top:22px;width:222px;font-family:"Archivo Narrow",sans-serif;font-size:9.6px;line-height:19.2px;letter-spacing:-.3px;color:#222}
.news-body a{color:var(--orange);text-decoration:none}
.news-body a.plain{color:#111}
.testi-title{left:430px;top:520px;width:212px}
.quote{left:302px;width:490px;height:117px;background:var(--white);border-radius:3px;box-shadow:0 1px 3px rgba(0,0,0,.22)}
.avatar{position:absolute;left:16px;top:14px;width:56px;height:56px;border-radius:50%}
.quote h3{position:absolute;left:89px;top:12px;font-size:13.5px;font-weight:700;color:#222}
.quote p{position:absolute;left:89px;top:38px;width:380px;font-size:9.8px;line-height:14.4px;color:#222}
.quote cite{position:absolute;left:89px;top:87px;font-style:normal;font-size:11px;color:var(--orange)}
.cat-col{list-style:none;font-size:11.5px;line-height:19.2px;color:var(--white)}
.cat-col .current{color:var(--orange)}
.region-nav{left:122px;top:1090px;display:flex;gap:22px;font-size:11.5px;color:var(--white)}
.region-nav .current{color:var(--orange)}
.share{left:295px;top:1132px;display:flex;gap:4px}
.share span{width:28px;height:28px;border-radius:50%;background:var(--white)}
.share span:first-child{background:var(--orange)}
</style>
</head>
<body>
<svg class="bands" width="816" height="1200" viewBox="0 0 816 1200">
  <defs>
    <linearGradient id="sandTop" x1="0" y1="0" x2="1" y2="1">
      <stop offset="0" stop-color="#c99a5c"/><stop offset=".5" stop-color="#e3c597"/><stop offset="1" stop-color="#d2a66b"/>
    </linearGradient>
    <linearGradient id="sandFoot" x1="0" y1="0" x2="1" y2="0">
      <stop offset="0" stop-color="#d6ad74"/><stop offset="1" stop-color="#e2c08c"/>
    </linearGradient>
  </defs>
  <polygon points="0,0 816,0 816,128 0,194" fill="url(#sandTop)" role="img" aria-label="Stone texture header"/>
  <polygon points="0,934 816,844 816,1200 0,1200" fill="url(#sandFoot)" role="img" aria-label="Stone texture footer"/>
  <polygon points="0,1042 816,1076 816,1200 0,1200" fill="#8a6438"/>
</svg>

<div class="abs brand"><span class="brand-mark"></span>Tarn Wisp</div>
<nav class="abs main-nav"><a href="#">Home</a><a class="current" href="#">About us</a><a href="#">Collections</a><a href="#">Contact us</a></nav>
<div class="abs account"><a href="#">Login</a>|<a href="#">Register</a></div>

<h2 class="abs section-title ancient-title">Ancient</h2>

<article class="abs card" style="left:23px"><div class="card-img" role="img" aria-label="Golden theatre mask" style="background:linear-gradient(135deg,#2a1a0c,#b8874a 55%,#3a2410)"></div>Lorem ipsum dolor sit amet,<br>consectetur adipiscing elit.<br>Sed dictum ante non diam<br>dignissim volutpat<a href="#">More...</a></article>
<article class="abs card" style="left:216px"><div class="card-img" role="img" aria-label="Bronze dancing deity statue" style="background:linear-gradient(135deg,#e4701a,#4a4a32 55%,#2c2a1c)"></div>Lorem ipsum dolor sit amet,<br>consectetur adipiscing elit.<br>Sed dictum ante non diam<br>dignissim volutpat<a href="#">More...</a></article>
<article class="abs card" style="left:414px"><div class="card-img" role="img" aria-label="Terracotta carved head" style="background:linear-gradient(135deg,#c9754a,#e0a27a 55%,#b8643c)"></div>Lorem ipsum dolor sit amet,<br>consectetur adipiscing elit.<br>Sed dictum ante non diam<br>dignissim volutpat<a href="#">More...</a></article>
<article class="abs card" style="left:606px"><div class="card-img" role="img" aria-label="Cameo portrait brooch" style="background:linear-gradient(135deg,#1c2a5a,#a8323a 45%,#e8dcc4 65%,#a8323a)"></div>Lorem ipsum dolor sit amet,<br>consectetur adipiscing elit.<br>Sed dictum ante non diam<br>dignissim volutpat<a href="#">More...</a></article>

<h2 class="abs section-title news-title">Latest News</h2>
<article class="abs news-item" style="top:556px">
  <div class="news-date">18<span>SEP</span></div>
  <h3 class="news-head">Lorem ipsum dolor sit amet, consectetur</h3>
  <p class="news-body">Phasellus dui lorem, dignissim nec justo et, dapibus rhoncus mauris. Fusce nulla leo, ultrices in neque bibendum, efficitur malesuada nisl. Ut maximus at nibh sit amet ultrices. Pellentesque magna massa, fermentum eu ipsum semper, consequat tempor ipsum. Donec posuere elit in ante gravida consequat ornare eu justo. Morbi ante diam, ultrices vel purus nec, vestibulum semper nisl. Nunc bibendum sed est at bibendum.<br><a href="#">Read More</a></p>
</article>
<article class="abs news-item" style="top:772px">
  <div class="news-date">18<span>SEP</span></div>
  <h3 class="news-head">Lorem ipsum dolor sit amet, consectetur</h3>
  <p class="news-body">Phasellus dui lorem, dignissim nec justo et, dapibus rhoncus mauris. Fusce nulla leo, ultrices in neque bibendum, efficitur malesuada nisl. Ut maximus at nibh sit amet ultrices. Pellentesque magna massa, fermentum eu ipsum semper, consequat tempor ipsum.<br><a class="plain" href="#">Read More</a></p>
</article>

<h2 class="abs section-title testi-title">Testimonial</h2>
<blockquote class="abs quote" style="top:581px">
  <div class="avatar" role="img" aria-label="Reader portrait" style="background:radial-gradient(circle,#e0b070,#7a5a30)"></div>
  <h3>“Praesent tempor luctus!”</h3>
  <p>JSuspendisse lobortis nunc sed urna scelerisque, vel maximus quam tincidunt. Vivamus nec accumsan ex, vitae consectetur ligula. Praesent tempor luctus eros. Sed dictum ante non diam dignissim volutpat.</p>
  <cite>Mara Quell</cite>
</blockquote>
<blockquote class="abs quote" style="top:709px">
  <div class="avatar" role="img" aria-label="Reader portrait" style="background:radial-gradient(circle,#e8d6b0,#b05a3a)"></div>
  <h3>“Sed dictum ante non!”</h3>
  <p>JSuspendisse lobortis nunc sed urna scelerisque, vel maximus quam tincidunt. Vivamus nec accumsan ex, vitae consectetur ligula. Praesent tempor luctus eros. Sed dictum ante non diam dignissim volutpat.</p>
  <cite>Dorian Pell</cite>
</blockquote>

<ul class="abs cat-col" style="left:113px;top:934px"><li>All Other Categories</li><li class="current">Ancient Art</li><li>Arms, Armor, and Militaria</li><li>Arts of the American West</li><li>Asian Art</li></ul>
<ul class="abs cat-col" style="left:347px;top:931px"><li>Books, Manuscripts, and Maps</li><li>Decorative Arts and Furniture</li><li>Ethnographic &amp; Tribal Arts</li><li>Fine Art</li><li>Folk Art and Americana</li></ul>
<ul class="abs cat-col" style="left:590px;top:922px"><li>Jewelry</li><li>Modern and Contemporary Art</li><li>Musical Instruments</li><li>Science and Natural History</li><li>Textile Arts</li></ul>

<nav class="abs region-nav"><span>Egyptian</span><span class="current">European</span><span>Medieval</span><span>Greek</span><span>Holy Land</span><span>Near Eastern</span><span>Romanian</span><span>Syrian</span><span>Greece</span></nav>
<div class="abs share" aria-label="Share links"><span></span><span></span><span></span><span></span></div>
</body>
</html>
```